Commercial Rooftop Solar business needs a website

We need a website with fantastic appeal for a new company based in Melbourne called Brightvale Energy. We design and install solar energy systems for commercial applications across Australia. Our market is to focus on small to medium businesses looking for solar solutions, but we will also provide our service for residential customers. We would like a beautiful 'front page' feel to our home page, using photographs of solar PV systems and/or natural imagery. Our logo uses the colours orange and black, which could easily be echoed in photographic imagery of sunset and sunrise, for example. The design should communicate quiet confidence and professionalism to a corporate marketplace.

NEW POINTS FOR BRIEF: This design also needs to be flexible to allow for additional future content, including a Support page with sub pages, FAQ's, and a Blog.

As part of this design project, we will require the coding for the website to be completed by the designer.

We have seen some websites, which we like the look and feel of: these are listed below.

keenroofpower.com.au:

• Beautiful images underlaying brief text selling points.
• Simple ‘front cover’ style home page with elegant drop-down menu, stylish simple font style.
• Home page invites exploration through the menu links, rather than trying to provide all the information up front.
• Company logo and name in the top left hand corner, contact details accessible at top right hand, seems consistent in most sites.

tolvaenergy.com.au

brinkeltpower.com:
• Same element as the others is the front-page style home page with beautiful images underlying text.

We have a webpage that we started uploading content to. You can use some of the content there in your designs: www.brightvaleenergy.com.au

Technical Specifications:
PAGES:

Home

About Us

Solutions - Commercial
- Residential

Products - Solar Panels - Morvo Falcon, Morvo CELT, Morvo KT
- Solar Inverters - Valtrex, SunPivot
- Monitoring systems - Lumen Metrics
- Batteries - QD

- Datasheets have been provided for reference but if it's too much work, you can use generic text and we will provide content later.

Contact Us

FUTURE PAGES (Please consider in structure, where links could be placed):

Support

FAQ's

Blog.

We could provide some content for the Support page soon, but the Blog and FAQ's are future pages which we don't want highlighted in the design as we don't yet have content.

Phone: 1800 7 VOLTA
Email: sales@brightvaleenergy.com.au

Currently, I do not have images and text available. Please
use placeholders in the meantime. The final text and images will be uploaded for the winner once a winning design has been selected.

Target Market(s)

Primary focus is on small to medium sized business owners. Those owners will have a house which may be suitable for solar so we want to cater to residential deeper in the website.

Industry/Entity Type

Solar Energy

Coding

Coded - Design and coding required

Number of Pages Required

5+ page

Colors
f78f20
0255a3

Requirements
Must have
• Logo as per attachments.
Nice to have
• Logo can have alternate colours Eg. White on Orange or Black etc. provided colour correct logo is shown somewhere eg. footer or contact page.
• In the active site, I'd like to have:
• Very slowly zooming images - barely perceptible.
• Title text that rolls into place
• Subtle movements
• See https://paylarkfinance.com.au/ for example

```html
<!DOCTYPE html>
<html lang="en">
<head>
<meta charset="utf-8">
<title>Brightvale Energy — Solar Energy Systems</title>
<link href="https://fonts.googleapis.com/css2?family=Raleway:wght@400;600;700;800&family=Open+Sans:wght@400;600;700&display=swap" rel="stylesheet">
<style>
:root{
  --orange:#ee5a24;
  --orange-dark:#d94b18;
  --ink:#2b2b2b;
  --text:#777;
  --light:#f1f1f1;
  --white:#fff;
  --footer-text:#fff3ea;
}
*{box-sizing:border-box;margin:0;padding:0}
html,body{width:1200px;height:2808px;overflow:hidden}
body{font-family:"Open Sans",Arial,sans-serif;color:var(--text);background:var(--white)}
h1,h2,h3,h4,.brand,.nav a,.btn{font-family:"Raleway",Arial,sans-serif}
.btn{display:inline-block;background:var(--orange);color:#fff;font-size:15px;font-weight:700;padding:14px 30px;text-transform:uppercase;letter-spacing:.5px}
.read{font-family:"Raleway",sans-serif;font-weight:800;font-size:14px;color:var(--ink);text-transform:uppercase}
.section-title{font-size:34px;font-weight:700;color:var(--ink);text-align:center;text-transform:uppercase;letter-spacing:1px}

/* hero */
.hero{position:relative;height:660px;background:linear-gradient(180deg,#f3a56a 0%,#d97a48 22%,#8e5a5a 40%,#2f3a5c 58%,#1e2a45 100%)}
.hero-photo{position:absolute;inset:0}
.topbar{position:absolute;top:0;left:0;right:0;height:104px;background:rgba(20,20,25,.55);display:flex;align-items:center;padding:0 70px}
.brand{display:flex;align-items:center;gap:12px;color:#fff;font-weight:800;font-size:24px;text-transform:uppercase;letter-spacing:.5px}
.brand-dot{width:26px;height:26px;border-radius:50%;background:var(--orange)}
.nav{display:flex;gap:50px;margin-left:auto;margin-right:60px}
.nav a{color:#fff;font-size:15px;font-weight:700;text-transform:uppercase;text-decoration:none}
.quick{color:#fff;font-size:13px;font-weight:700;text-transform:uppercase}
.quick .phone{display:block;color:var(--orange);font-size:24px;font-weight:700;margin-top:2px}
.hero-center{position:absolute;top:230px;left:0;right:0;text-align:center}
.hero-center .brand{justify-content:center;font-size:48px}
.hero-center .brand-dot{width:46px;height:46px}
.hero-title{margin:40px 0 26px;color:#fff;font-size:46px;font-weight:800;text-transform:uppercase;letter-spacing:1px}
.dots{position:absolute;bottom:36px;left:0;right:0;display:flex;justify-content:center;gap:14px}
.dots span{width:14px;height:14px;border-radius:50%;background:rgba(255,255,255,.55)}
.dots span.on{background:#fff}
.arrow{position:absolute;top:170px;width:34px;height:34px;border-radius:4px;background:rgba(255,255,255,.25)}

/* welcome */
.welcome{height:320px;display:flex;padding:80px 70px 0}
.welcome-head{width:340px}
.welcome-head h2{font-size:34px;font-weight:800;color:var(--ink);text-transform:uppercase}
.welcome-head .brand{color:var(--orange);font-size:30px;margin:12px 0 30px}
.welcome-head .brand-dot{width:24px;height:24px}
.welcome p{width:730px;font-size:15px;line-height:1.75;padding-left:30px;border-left:3px solid var(--orange)}

/* solutions */
.solutions{height:380px;background:var(--light);padding-top:26px}
.cards{display:flex;justify-content:center;gap:40px;margin-top:30px}
.card{width:340px;height:280px;background:#fff;text-align:center;padding:30px 26px 0}
.card svg{height:64px}
.card h3{color:var(--orange);font-size:19px;font-weight:800;text-transform:uppercase;margin:12px 0 12px}
.card p{font-size:14px;line-height:1.6;margin-bottom:14px}

/* band */
.band{position:relative;height:280px;background:linear-gradient(180deg,#5b6f86 0%,#3c4b60 55%,#223044 100%);text-align:center;padding-top:80px}
.band h2{color:#fff;font-size:38px;font-weight:700;text-transform:uppercase;line-height:1.25}
.band .btn{margin-top:22px}

/* blog */
.blog{height:520px;padding-top:48px}
.posts{display:flex;justify-content:center;gap:40px;margin-top:56px}
.post{width:340px}
.post-img{height:220px}
.post h4{color:var(--orange);font-size:17px;font-weight:800;text-transform:uppercase;line-height:1.35;margin:20px 0 8px}
.post .meta{font-size:12px;margin-bottom:18px}

/* testimonials */
.testimonials{position:relative;height:400px;padding-top:30px;text-align:center}
.avatar{width:92px;height:92px;border-radius:50%;background:linear-gradient(160deg,#d8d2cb,#5a5f6a);margin:26px auto 18px}
.quote{width:960px;margin:0 auto;font-size:15px;line-height:1.75;font-style:italic}
.author{color:var(--orange);font-size:13px;font-weight:700;text-transform:uppercase;margin-top:12px}
.t-arrow{position:absolute;top:230px;font-size:40px;color:#888;font-family:"Raleway",sans-serif}

/* footer */
.footer{height:248px;background:var(--orange);color:var(--footer-text);display:flex;padding:40px 70px 0;gap:60px;font-size:13px}
.footer h4{color:#fff;font-size:15px;font-weight:800;text-transform:uppercase;margin-bottom:12px}
.footer .brand{font-size:22px}
.footer .brand-dot{background:#fff}
.footer li{list-style:none;line-height:1.8}
.f-brand{width:300px}
.f-brand p{margin-top:20px;line-height:1.6}
.f-nav{width:150px}
.f-contact{width:260px}
.signup{display:flex;margin-top:6px}
.signup span{width:200px;height:40px;background:#fff;color:#999;padding:11px 12px}
.signup b{margin-left:6px;background:#1d1d1d;color:#fff;padding:11px 16px;font-family:"Raleway",sans-serif}
</style>
</head>
<body>

<section class="hero">
  <div class="hero-photo" role="img" aria-label="Rooftop solar panels at sunset"></div>
  <header class="topbar">
    <div class="brand"><span class="brand-dot"></span>Brightvale Energy</div>
    <nav class="nav"><a>Home</a><a>About Us</a><a>Solutions</a><a>Contact Us</a></nav>
    <div class="quick">Quick Contact:<span class="phone">1-800-555-0142</span></div>
  </header>
  <span class="arrow" style="left:150px"></span>
  <span class="arrow" style="right:150px"></span>
  <div class="hero-center">
    <div class="brand"><span class="brand-dot"></span>Brightvale Energy</div>
    <h1 class="hero-title">We Design &amp; Install Solar Energy Systems</h1>
    <span class="btn">Contact Us</span>
  </div>
  <div class="dots"><span></span><span class="on"></span><span></span><span></span></div>
</section>

<section class="welcome">
  <div class="welcome-head">
    <h2>Welcome To</h2>
    <div class="brand"><span class="brand-dot"></span>Brightvale Energy</div>
    <span class="btn">Read More</span>
  </div>
  <p>We design and install solar energy systems for small and medium businesses across Australia. From the first roof survey to final handover, our team plans every array around how your site uses power through the day. We choose proven panels, inverters and batteries, then monitor each system so it keeps delivering. Our installers are accredited and our quotes are clear, with no surprises later. Whether you run a warehouse, an office or a workshop, we help you cut running costs and lower emissions with a system built to last for decades of reliable service.</p>
</section>

<section class="solutions">
  <h2 class="section-title">Our Solutions</h2>
  <div class="cards">
    <div class="card">
      <svg viewBox="0 0 64 64" width="64"><g stroke="#333" stroke-width="6" stroke-linecap="round"><line x1="12" y1="52" x2="44" y2="20"/><line x1="14" y1="14" x2="52" y2="52"/></g><circle cx="48" cy="16" r="9" fill="none" stroke="#333" stroke-width="5"/></svg>
      <h3>Design and Install</h3>
      <p>Tailored system design and tidy installation by accredited crews on every site.</p>
      <span class="read">Read More</span>
    </div>
    <div class="card">
      <svg viewBox="0 0 64 64" width="64"><rect x="18" y="4" width="28" height="56" fill="#333"/><g fill="#fff"><rect x="23" y="10" width="6" height="6"/><rect x="35" y="10" width="6" height="6"/><rect x="23" y="22" width="6" height="6"/><rect x="35" y="22" width="6" height="6"/><rect x="23" y="34" width="6" height="6"/><rect x="35" y="34" width="6" height="6"/><rect x="28" y="48" width="8" height="12"/></g></svg>
      <h3>Commercial</h3>
      <p>Rooftop arrays sized for offices, factories and retail sites of every scale.</p>
      <span class="read">Read More</span>
    </div>
    <div class="card">
      <svg viewBox="0 0 64 64" width="64"><path d="M32 6 4 32h8v26h16V42h8v16h16V32h8z" fill="#333"/></svg>
      <h3>Residential</h3>
      <p>Quiet, efficient home systems with batteries and monitoring as you need.</p>
      <span class="read">Read More</span>
    </div>
  </div>
</section>

<section class="band" role="img" aria-label="City skyline across the harbour at dusk">
  <h2>Solar Energy Systems for Commercial<br>Applications Across Australia</h2>
  <span class="btn">Read More</span>
</section>

<section class="blog">
  <h2 class="section-title">Blog Posts</h2>
  <div class="posts">
    <article class="post">
      <div class="post-img" role="img" aria-label="Technician beside a solar panel" style="background:linear-gradient(180deg,#8fb7d8,#6b8aa3 60%,#9c6a4e)"></div>
      <h4>How rooftop solar lowers business running costs</h4>
      <div class="meta">June 22, 2017 &nbsp;|&nbsp; By Admin</div>
      <span class="read">Read More</span>
    </article>
    <article class="post">
      <div class="post-img" role="img" aria-label="Solar panels on a tiled roof under blue sky" style="background:linear-gradient(180deg,#5d93c9,#3d5f86 55%,#b2552e)"></div>
      <h4>Choosing the right inverter for your site</h4>
      <div class="meta">June 22, 2017 &nbsp;|&nbsp; By Admin</div>
      <span class="read">Read More</span>
    </article>
    <article class="post">
      <div class="post-img" role="img" aria-label="Installers fitting panels on a roof at sunset" style="background:linear-gradient(180deg,#f2c07a,#e08a3c 50%,#6b6f7a)"></div>
      <h4>What to expect on installation day at work</h4>
      <div class="meta">June 22, 2017 &nbsp;|&nbsp; By Admin</div>
      <span class="read">Read More</span>
    </article>
  </div>
</section>

<section class="testimonials">
  <h2 class="section-title">Customer Testimonials</h2>
  <div class="avatar" role="img" aria-label="Customer portrait"></div>
  <p class="quote">“ The team handled our warehouse system from start to finish with real care. The design was explained clearly, the crew were tidy and on time, and our power bills dropped from the very first quarter. We would happily recommend them to any business thinking about solar for their premises. ”</p>
  <div class="author">Daniel Hartwell</div>
  <span class="t-arrow" style="left:70px">‹</span>
  <span class="t-arrow" style="right:70px">›</span>
</section>

<footer class="footer">
  <div class="f-brand">
    <div class="brand"><span class="brand-dot"></span>Brightvale Energy</div>
    <p>Copyright © 2017<br>Brightvale Energy<br>Privacy Policy &nbsp;|&nbsp; Terms and Conditions</p>
  </div>
  <div class="f-nav">
    <h4>Navigation</h4>
    <ul><li>Home</li><li>About Us</li><li>Solutions</li><li>Contact Us</li></ul>
  </div>
  <div class="f-contact">
    <h4>Contact Info</h4>
    <ul><li>12 Harbour Lane,</li><li>Melbourne VIC 3000</li><li>1-800-555-0142</li><li>info@brightvaleenergy.com.au</li></ul>
  </div>
  <div class="f-news">
    <h4>Newsletter Sign Up</h4>
    <div class="signup"><span>Enter Email Address</span><b>SIGN UP</b></div>
  </div>
</footer>

</body>
</html>
```